Wine Radio Show web re-design

We need new website look for an unconventional, nationally-syndicated WINE RADIO show. Show is fun, hip, witty and covers all wine lifestyle topics. We are redesigning logo and looking for a redesign of our wordpress site that hosts all our audio podcasts, and the site design needs to leverage and maximize these podcasts. Do NOT use the logo currently on the website. The site is corklantern.com, please see more info on the attached.

Do NOT use the logo currently on the website. Please just typeset the name "Cork Lantern Radio".
Updates

Please do NOT use the logo from the current website. Please just use type (to match theme/deisgn) "Cork Lantern Radio". Thank you.

Hello Designers, Thank you for working on this project. A piece of feedback overall is that we'd like much less image/masthead space in general (the photos and images at the top). We'd like the navigation and the latest Cork Lantern podcast to be above the fold. Most of the wine imagery/scenery shots can be minimalized/drastically reduced/eliminated, to allow more room for the different sections. Hope that makes sense, and again, thank you for working on this!! Marla

Target Market(s)

Wine lovers and wine industry professionals, probably 30+ years old

Industry/Entity Type

Radio

Font styles to use
Serif
Sans Serif
Decorative
Other font styles liked:
• Modern retro fonts

Requirements
Must have
• Must keep current content of site:
http://corklanternradio.com/podcast/
Feature podcasts prominently.
Do NOT use the logo currently on the website.
Nice to have
• Graphics to consider incorporating:
• WINE: Grapes, wine glasses, wine bottles, wine pouring, corkscrews, grapevines, vineyards
• RADIO symbols: soundwaves, antenna, radio icon, Podcast symbols, microphone
Should not have
• Do NOT use current logo - just use type.

```html
<!DOCTYPE html>
<html lang="en">
<head>
<meta charset="utf-8">
<title>Cork Lantern Radio</title>
<link href="https://fonts.googleapis.com/css2?family=Dosis:wght@500;600;700&family=Open+Sans:wght@400;600;700&display=swap" rel="stylesheet">
<style>
:root{
  --wine:#b3141c;
  --sky:#3d95d9;
  --gold:#d9a90b;
  --ink:#333;
  --muted:#777;
  --line:#dcdcdc;
  --paper:#f3f2ef;
  --card:#fff;
  --dark:#1f1f1f;
  --fb:#3b5b98;
}
*{box-sizing:border-box;margin:0;padding:0}
html,body{width:1200px;height:3600px;overflow:hidden}
body{position:relative;background:var(--paper);font-family:"Open Sans",Arial,sans-serif;color:var(--ink);font-size:14px;line-height:1.5}
.art{position:absolute}
.masthead-wash{left:0;top:0;width:1200px;height:130px;background:linear-gradient(180deg,#dedbd5 0%,#ebe8e3 60%,var(--paper) 100%)}
.page{position:absolute;left:186px;top:0;width:834px}
.site-head{padding-top:26px;position:relative}
.brand{display:flex;align-items:center;gap:12px;height:44px}
.brand-dot{width:40px;height:40px;border-radius:50%;background:var(--wine)}
.brand-name{font-family:"Dosis",Arial,sans-serif;font-weight:700;font-size:34px;line-height:1;color:var(--wine);letter-spacing:.5px}
.main-nav{margin-top:14px;height:32px;display:flex;align-items:center;justify-content:space-between;border-top:1px solid var(--line);border-bottom:1px solid var(--line)}
.main-nav a{font-family:"Dosis",Arial,sans-serif;font-weight:700;font-size:15px;color:var(--wine);text-decoration:none;text-transform:uppercase}
.columns{display:flex;gap:15px;margin-top:14px;align-items:flex-start}
.main-col{width:588px;flex:none}
.side-col{width:231px;flex:none}
.hero{position:relative;height:220px;overflow:hidden}
.hero-art{width:100%;height:100%;background:linear-gradient(160deg,#6f8f3c 0%,#4b6b2a 40%,#8a2a3a 70%,#c8a36a 100%)}
.hero-caption{position:absolute;left:0;bottom:0;width:100%;height:36px;background:rgba(20,20,20,.75);color:#fff;font-family:"Dosis",Arial,sans-serif;font-weight:600;font-size:18px;display:flex;align-items:center;justify-content:center}
.hero-arrow{position:absolute;top:78px;width:30px;height:30px;border-radius:50%;background:rgba(0,0,0,.45)}
.hero-arrow svg{display:block;margin:8px}
.section-head{margin-top:14px;height:30px;background:var(--sky);color:#fff;font-family:"Dosis",Arial,sans-serif;font-weight:700;font-size:19px;padding-left:14px;line-height:30px}
.card{margin-top:6px;background:var(--card);border:1px solid #e4e4e4;padding-bottom:26px}
.ep-title{display:flex;gap:14px;padding:20px 22px 6px}
.ep-icon{flex:none;width:40px;height:40px;border-radius:50%;background:var(--wine);position:relative}
.ep-icon svg{position:absolute;left:11px;top:11px}
.ep-title h2{font-family:"Dosis",Arial,sans-serif;font-weight:600;font-size:26px;line-height:1.25;color:var(--ink)}
.meta{font-size:11px;color:var(--muted);padding:2px 0 0 76px}
.meta em{font-style:normal;color:var(--wine)}
.ep-body{position:relative;margin-top:18px}
.share{position:absolute;left:18px;top:0;width:46px}
.share span{display:block;height:22px;border:1px solid var(--line);margin-bottom:6px;font-size:9px;text-align:center;line-height:20px;color:var(--muted);background:#fafafa}
.ep-photo{margin-left:69px;width:495px;background:linear-gradient(160deg,#d9c39b,#b38c5c 45%,#6f5a3c)}
.ep-text{margin:14px 22px 0 69px;font-size:12px;color:var(--muted);line-height:1.6}
.btn{display:inline-block;background:#8a8a8a;color:#fff;font-size:11px;font-weight:600;padding:3px 16px;border-radius:2px}
.center{text-align:center}
.guest{display:flex;align-items:center;gap:20px;margin:0 40px 0 90px;padding:14px 0}
.guest .pic{flex:none;width:66px;height:66px;border-radius:50%;background:linear-gradient(180deg,#b8b2aa,#6f6a64)}
.guest p{font-size:11px;color:var(--muted);line-height:1.55}
.guest strong{display:block;font-family:"Dosis",Arial,sans-serif;font-weight:600;color:var(--ink);font-size:13px;margin-top:3px}
.player{margin:24px 28px 0;height:30px;background:var(--dark);display:flex;align-items:center;gap:10px;padding:0 10px}
.player .track{flex:1;height:4px;background:#555;position:relative}
.player .track::before{content:"";position:absolute;left:0;top:0;width:22%;height:4px;background:var(--wine)}
.mini-grid{display:grid;grid-template-columns:287px 287px;gap:14px;margin-top:14px}
.mini{background:var(--card);border:1px solid #e4e4e4;padding-bottom:20px}
.mini .ep-title{padding:18px 14px 4px;gap:10px}
.mini .ep-title h2{font-size:21px}
.mini .ep-icon{width:34px;height:34px}
.mini .ep-icon svg{left:8px;top:8px}
.mini .meta{padding-left:58px}
.mini .rule{border-top:1px solid var(--line);margin:12px 14px}
.mini p{font-size:12px;color:var(--muted);padding:0 14px;line-height:1.55}
.mini .btnrow{text-align:center;margin-top:16px}
.host-photo{height:150px;background:linear-gradient(180deg,#8fb3d6,#4d7fa6 60%,#2e4660)}
.host-tag{margin-top:8px;background:var(--gold);color:#fff;font-family:"Dosis",Arial,sans-serif;font-weight:700;font-size:17px;text-align:center;height:30px;line-height:30px}
.host p{font-size:12px;color:var(--muted);margin:10px 4px;line-height:1.55}
.social-counts{margin-top:16px;display:flex;justify-content:space-around;text-align:center;font-size:11px;color:var(--muted);line-height:1.3}
.social-counts span{display:block;width:44px;height:44px;border-radius:50%;background:var(--sky);margin:0 auto 4px}
.social-counts span.c2{background:var(--fb)}
.ads{margin-top:14px;display:grid;grid-template-columns:110px 110px;gap:11px}
.ads .stack{display:flex;flex-direction:column;gap:10px}
.ad{border-radius:2px}
.subscribe{margin-top:16px;display:flex;align-items:center;gap:10px;font-family:"Dosis",Arial,sans-serif;font-weight:700;font-size:16px;color:var(--ink)}
.subscribe i{width:34px;height:34px;border-radius:50%;background:var(--sky);display:block}
.side-box{margin-top:14px;background:var(--card)}
.side-head{background:var(--gold);color:#fff;font-family:"Dosis",Arial,sans-serif;font-weight:700;font-size:18px;text-align:center;height:32px;line-height:32px}
.side-list{list-style:none;padding:10px 12px;font-size:12px}
.side-list li{padding:3px 0}
.side-list .sub{padding-left:18px;color:var(--muted)}
.side-list .sub2{padding-left:36px;color:var(--wine)}
.recent li a,.uncorked-list li a{color:var(--wine);text-decoration:none;display:block;line-height:1.35}
.recent li,.uncorked-list li{border-bottom:1px solid var(--line);padding:6px 0}
.date{color:var(--muted);font-size:11px}
.fb-widget{margin:10px 12px;border:1px solid var(--line);padding:8px;font-size:11px;color:var(--muted)}
.fb-widget b{color:var(--fb);font-size:13px;display:flex;align-items:center;gap:8px}
.fb-widget b i{width:30px;height:30px;background:var(--wine);display:block}
.fb-faces{display:grid;grid-template-columns:repeat(5,1fr);gap:5px;margin-top:8px}
.fb-faces span{height:30px;background:#c9ccd3}
.follow-row{display:flex;justify-content:center;gap:10px;padding:12px}
.follow-row span{width:30px;height:30px;border-radius:50%;background:var(--sky)}
.follow-row span:nth-child(1){background:var(--fb)}
.follow-row span:nth-child(3){background:#c4302b}
.follow-row span:nth-child(4){background:#2f8c3c}
.site-foot{position:absolute;left:0;top:3568px;width:1200px;height:32px;background:var(--dark);color:#aaa;font-size:10px;display:flex;align-items:center;justify-content:space-between;padding:0 186px}
</style>
</head>
<body>

<div class="art masthead-wash"></div>
<div class="art" role="img" aria-label="Glass of red wine being poured" style="left:0;top:0;width:150px;height:170px;background:linear-gradient(180deg,#e6e2dc,#c9a9a9 50%,#8d1a22)"></div>
<div class="art" role="img" aria-label="Wine bottle, glasses and grapes still life" style="left:640px;top:0;width:150px;height:70px;background:linear-gradient(180deg,#e4e0da,#b39a8c 60%,#6b3a3a);opacity:.8"></div>
<div class="art" role="img" aria-label="Vintage tabletop radio" style="left:820px;top:0;width:200px;height:76px;background:linear-gradient(160deg,#c7a27a,#8a5a34 60%,#4a3020)"></div>
<div class="art" role="img" aria-label="Glass of red wine" style="left:1110px;top:0;width:90px;height:170px;background:linear-gradient(180deg,#e6e2dc,#b76a70 55%,#8d1a22)"></div>

<div class="page">
  <header class="site-head">
    <div class="brand"><span class="brand-dot"></span><span class="brand-name">Cork Lantern Radio</span></div>
    <nav class="main-nav">
      <a>Home</a><a>Episode Archives ▾</a><a>Uncorked</a><a>About the Show ▾</a><a>About the Host ▾</a><a>On the Air ▾</a><a>Blog</a><a>Store</a><a>Contact</a>
    </nav>
  </header>

  <div class="columns">
    <main class="main-col">
      <section class="hero">
        <div class="hero-art" role="img" aria-label="Red wine bottle, glasses and grapes on a table in a vineyard"></div>
        <span class="hero-arrow" style="left:10px"><svg width="14" height="14" viewBox="0 0 14 14"><path d="M9 2 4 7l5 5" stroke="#fff" stroke-width="2" fill="none"/></svg></span>
        <span class="hero-arrow" style="right:10px"><svg width="14" height="14" viewBox="0 0 14 14"><path d="m5 2 5 5-5 5" stroke="#fff" stroke-width="2" fill="none"/></svg></span>
        <div class="hero-caption">The longest fine wine region on the planet is Spain</div>
      </section>

      <div class="section-head">This week on Cork Lantern:</div>
      <article class="card">
        <div class="ep-title">
          <span class="ep-icon"><svg width="18" height="18" viewBox="0 0 18 18"><rect x="1" y="3" width="16" height="14" rx="1" fill="none" stroke="#fff" stroke-width="2"/><path d="M1 7h16M5 1v4M13 1v4" stroke="#fff" stroke-width="2"/></svg></span>
          <h2>Episode #254 – All Work and Play Gives You Plenty to Wine About!</h2>
        </div>
        <div class="meta">Posted by <em>Cork Lantern</em> &nbsp; June 7, 2014 &nbsp; <em>Episode Archives</em></div>
        <div class="ep-body">
          <div class="share"><span>Like 0</span><span>Post 0</span><span>+1</span><span>Share</span><span>Pin</span><span>Email</span></div>
          <div class="ep-photo" role="img" aria-label="Winemaker in a straw hat seated beside wine bottles and a glass of red" style="height:360px"></div>
          <p class="ep-text">The weather is warming up. Does your preference in wine transition when the temps rise? Many people tend to make a shift, and that includes Coastline Living wine editor Lena Marsh. Host Reid Calloway welcomes her back for a discussion about how red wine runs a bit heavy for summer.</p>
          <div class="center" style="margin:16px 0 18px"><span class="btn">View More</span></div>
        </div>
        <div class="guest"><span class="pic" role="img" aria-label="Guest portrait"></span><p>The weather is warming up. Does your preference in wine transition when the temps rise? Many people tend to make a shift, and that includes Coastline Living wine editor Lena Marsh.<strong>Lena Marsh, Wine Editor, Coastline Living</strong></p></div>
        <div class="guest"><p>Next, you'll meet a winemaker who pursued a job at one of the great wineries across several continents. Much of Owen's talent is in matching terroir to vine, so look for some fascinating conversation with the namesake of Strathmore Vineyards!<strong>Owen Strathmore, Owner of Strathmore Vineyards</strong></p><span class="pic" role="img" aria-label="Guest portrait"></span></div>
        <div class="guest"><span class="pic" role="img" aria-label="Guest portrait"></span><p>One brand that is very well known from coast to coast for its quality wines is Hollis Winery from the Paso Robles region of California's central coast. Reid whets your appetite for excellent wine, an extraordinary culinary experience and a remarkable vacation.<strong>Theo Antonakis, Wine Educator, Hollis Winery</strong></p></div>
        <div class="guest"><p>Getaway as he talks with Hollis's wine educator Theo Antonakis and guest relations manager Celia Dumont, both certified sommeliers. Find out how Hollis became one of the world's top 5 places to come stay and enjoy food and wine.<strong>Celia Dumont, Guest Services Mgr, Hollis Winery</strong></p><span class="pic" role="img" aria-label="Guest portrait"></span></div>
        <div class="player">
          <svg width="70" height="14" viewBox="0 0 70 14"><path d="M0 1l10 6-10 6z" fill="#fff"/><rect x="18" y="1" width="11" height="12" fill="#fff"/><path d="M38 1l7 6-7 6zM46 1l7 6-7 6z" fill="#fff"/><rect x="55" y="1" width="2" height="12" fill="#fff"/></svg>
          <span class="track"></span>
          <svg width="16" height="14" viewBox="0 0 16 14"><path d="M0 4h4l5-4v14l-5-4H0z" fill="#fff"/><path d="M11 3c2 2 2 6 0 8" stroke="#fff" fill="none" stroke-width="1.5"/></svg>
        </div>
      </article>

      <div class="section-head">Most Recent Episodes:</div>
      <article class="card">
        <div class="ep-title">
          <span class="ep-icon"><svg width="18" height="18" viewBox="0 0 18 18"><rect x="1" y="3" width="16" height="14" rx="1" fill="none" stroke="#fff" stroke-width="2"/><path d="M1 7h16M5 1v4M13 1v4" stroke="#fff" stroke-width="2"/></svg></span>
          <h2>Episode #252 – The Inside Scoop on China's Extraordinary Growth and Passion for Wine</h2>
        </div>
        <div class="meta">Posted by <em>Cork Lantern</em> &nbsp; May 24, 2014 &nbsp; <em>Episode Archives</em></div>
        <div class="ep-body">
          <div class="share"><span>Like 0</span><span>Post 0</span><span>+1</span><span>Share</span><span>Pin</span><span>Email</span></div>
          <div class="ep-photo" role="img" aria-label="Two wine experts holding glasses of white wine" style="height:380px;background:linear-gradient(160deg,#9fbf8a,#5f7f52 50%,#3a4a38)"></div>
          <p class="ep-text">This week on Cork Lantern Radio, host Reid Calloway speaks with two of the biggest experts on the growing popularity of wine in Asia. Felix Wong is the preeminent wine educator in China, Hong Kong and Singapore.</p>
          <div class="center" style="margin-top:16px"><span class="btn">View More</span></div>
        </div>
      </article>

      <div class="mini-grid">
        <article class="mini">
          <div class="ep-title"><span class="ep-icon"><svg width="18" height="18" viewBox="0 0 18 18"><rect x="1" y="3" width="16" height="14" rx="1" fill="none" stroke="#fff" stroke-width="2"/><path d="M1 7h16M5 1v4M13 1v4" stroke="#fff" stroke-width="2"/></svg></span><h2>Uncorked #630 – Celebrity Tipples</h2></div>
          <div class="meta">Posted by <em>Cork Lantern</em> &nbsp; May 29, 2014</div>
          <div class="rule"></div>
          <p>Ever wondered what your favorite actor's favorite wine is? Well, we've got a few to reveal on this edition of UNCORKED.</p>
          <div class="btnrow"><span class="btn">View More</span></div>
        </article>
        <article class="mini">
          <div class="ep-title"><span class="ep-icon"><svg width="18" height="18" viewBox="0 0 18 18"><rect x="1" y="3" width="16" height="14" rx="1" fill="none" stroke="#fff" stroke-width="2"/><path d="M1 7h16M5 1v4M13 1v4" stroke="#fff" stroke-width="2"/></svg></span><h2>Uncorked #629 – Fermented Fruit</h2></div>
          <div class="meta">Posted by <em>Cork Lantern</em> &nbsp; June 05, 2014</div>
          <div class="rule"></div>
          <p>Did you know that there is a large array of wines made from fruits other than the grape? Find out more on this installment of UNCORKED.</p>
          <div class="btnrow"><span class="btn">View More</span></div>
        </article>
        <article class="mini">
          <div class="ep-title"><span class="ep-icon"><svg width="18" height="18" viewBox="0 0 18 18"><rect x="1" y="3" width="16" height="14" rx="1" fill="none" stroke="#fff" stroke-width="2"/><path d="M1 7h16M5 1v4M13 1v4" stroke="#fff" stroke-width="2"/></svg></span><h2>Uncorked #628 – The Champagne Oscars</h2></div>
          <div class="meta">Posted by <em>Cork Lantern</em> &nbsp; May 28, 2014</div>
          <div class="rule"></div>
          <p>Step aside, Hollywood. A new competition to celebrate the best of bubbles is being hailed as the Oscars of the Champagne world.</p>
          <div class="btnrow"><span class="btn">View More</span></div>
        </article>
        <article class="mini">
          <div class="ep-title"><span class="ep-icon"><svg width="18" height="18" viewBox="0 0 18 18"><rect x="1" y="3" width="16" height="14" rx="1" fill="none" stroke="#fff" stroke-width="2"/><path d="M1 7h16M5 1v4M13 1v4" stroke="#fff" stroke-width="2"/></svg></span><h2>Uncorked #626 – Unusual Tastes</h2></div>
          <div class="meta">Posted by <em>Cork Lantern</em> &nbsp; May 22, 2014</div>
          <div class="rule"></div>
          <p>Step aside, Hollywood. A new competition to celebrate the best of bubbles is being hailed as the Oscars of the Champagne world.</p>
          <div class="btnrow"><span class="btn">View More</span></div>
        </article>
      </div>
    </main>

    <aside class="side-col">
      <div class="host">
        <div class="host-photo" role="img" aria-label="Portrait of the show host outdoors"></div>
        <div class="host-tag">host Reid Calloway</div>
        <p>Reid Calloway's public speaking career began in high school when he won an award-winning orator and debater. Reid went on to compete in speech and debate at Seabrook University's coastal campus.</p>
        <div class="center"><span class="btn">View More</span></div>
      </div>

      <div class="social-counts">
        <div><span></span>9930<br>Followers</div>
        <div><span class="c2"></span>31<br>Fans</div>
        <div><span></span>50<br>Subscribe</div>
      </div>

      <div class="ads">
        <div class="stack">
          <div class="ad" style="height:170px;background:linear-gradient(180deg,#c01d24,#e7d9c8)"></div>
          <div class="ad" style="height:80px;background:#5a5a5a"></div>
          <div class="ad" style="height:130px;background:linear-gradient(180deg,#f1e6d6,#c01d24)"></div>
        </div>
        <div class="ad" style="height:400px;background:linear-gradient(180deg,#efe4cf,#c9b38a 45%,#6b2b44)"></div>
      </div>

      <div class="subscribe"><i></i>Subscribe on Podstand</div>

      <div class="side-box">
        <div class="side-head">Archives</div>
        <ul class="side-list">
          <li>▾ Archives 2014 (66)</li>
          <li class="sub">▾ June (1)</li>
          <li class="sub2">All Work and Play Gives You Plenty to Wine About!</li>
          <li class="sub">▸ May (5)</li>
          <li class="sub">▸ April (6)</li>
          <li class="sub">▸ March (5)</li>
          <li class="sub">▸ February (4)</li>
          <li class="sub">▸ January (4)</li>
          <li>▸ Archives 2013 (52)</li>
          <li>▸ Archives 2012 (52)</li>
          <li>▸ Archives 2011 (52)</li>
          <li>▸ Archives 2010 (52)</li>
          <li>▸ Archives 2009 (48)</li>
          <li>▸ Archives 2008 (30)</li>
        </ul>
      </div>

      <div class="side-box">
        <div class="side-head">Recent Shows</div>
        <ul class="side-list recent">
          <li><a>Episode #254 – All Work and Play Gives You Plenty to Wine About!</a><span class="date">June 7, 2014</span></li>
          <li><a>Episode #253 – Knowing Wine From Wing: The Expert Storyteller at Vinelist</a><span class="date">May 31, 2014</span></li>
          <li><a>Episode #252 – The Inside Scoop on China's Extraordinary Growth and Passion for Wine</a><span class="date">May 24, 2014</span></li>
          <li><a>Episode #251 – The Largest Fine Wine Region on the Planet is Spain's Heartland</a><span class="date">May 17, 2014</span></li>
        </ul>
      </div>

      <div class="side-box">
        <div class="side-head">Our Friendbook Page</div>
        <div class="fb-widget">
          <b><i></i>Cork Lantern Radio</b>
          <div style="margin-top:4px">231 people like Cork Lantern Radio</div>
          <div class="fb-faces"><span></span><span></span><span></span><span></span><span></span><span></span><span></span><span></span><span></span><span></span></div>
        </div>
      </div>

      <div class="side-box">
        <div class="side-head">Follow us</div>
        <div class="follow-row"><span></span><span></span><span></span><span></span><span></span></div>
      </div>

      <div class="side-box">
        <div class="side-head">Uncorked</div>
        <ul class="side-list uncorked-list">
          <li><a>Uncorked #630 – Celebrity Tipples</a><span class="date">June 6, 2014</span></li>
          <li><a>Uncorked #629 – Fermented Fruit</a><span class="date">June 5, 2014</span></li>
          <li><a>Uncorked #628 – The Champagne Oscars</a><span class="date">June 4, 2014</span></li>
          <li><a>Uncorked #627 – Three Wine Regions</a><span class="date">June 3, 2014</span></li>
        </ul>
      </div>
    </aside>
  </div>
</div>

<div class="art" role="img" aria-label="Corkscrew with a cork" style="left:0;top:3330px;width:130px;height:238px;background:linear-gradient(200deg,#e0ddd8,#a58a6a 60%,#6b5138)"></div>
<div class="art" role="img" aria-label="Bottle of white wine with a lime" style="left:1090px;top:3300px;width:110px;height:268px;background:linear-gradient(180deg,#e6e4de,#c9d69a 50%,#7c9a3a)"></div>

<footer class="site-foot">
  <span>Copyright © Cork Lantern Radio 2014. All Rights Reserved.</span>
  <span>Home | Episode Archives | Uncorked | About the Show | About the Host | On the Air | Blog | Store | Contact</span>
</footer>

</body>
</html>
```